Corvella Web Design Project

I am attaching my logo so I need to see applied to the website developed by you guys!!
Tbahks!!
Ferruccio
This is the DNA of the company
Flat and dynamic organization - Informal and respectful social approac
Innovative - Always striving for the best solution
Reliability and Quality - The value of our name
Flexibility - Ability to handle new requirements and unforeseen events
Simplicity - Technology must serve – NOT rule!
Cooperative Relations - The synergy that makes 1+1=3
We still don´t have our logo as we have another open project on artbazaarly
Our company won´t be selling this equipment but providing welding services for shipyard industry, as you can see on the website below.
www.velmorasystems.example
Reason: Hi webdesigners,
I will be deciding my logo by this weekend as soon as I have decided I will post my logo to see it applied to your design!!!
Thanks
Ferruccio
I just Sent my logo for your attention!!!!
Welding

```html
<!DOCTYPE html>
<html lang="en">
<head>
<meta charset="utf-8">
<title>Corvella — Welding Services</title>
<link href="https://fonts.googleapis.com/css2?family=Mulish:wght@300;400;500&display=swap" rel="stylesheet">
<style>
:root{
  --teal-top:#1492b0;
  --teal-bottom:#0a6887;
  --heading:#1a6f8c;
  --sub:#4a4a4a;
  --body:#8a8a8a;
  --white:#ffffff;
  --caption-bg:rgba(0,0,0,0.72);
  --card-band:rgba(16,90,150,0.82);
  --orange-top:#f5b01a;
  --orange-bottom:#e58d05;
  --footer-bg:#f4f4f4;
  --footer-line:#dddddd;
  --footer-text:#333333;
  --footer-muted:#666666;
  --social:#3a6fb0;
}
*{margin:0;padding:0;box-sizing:border-box}
html,body{width:1200px;height:1166px;overflow:hidden;background:var(--white)}
body{position:relative;font-family:"Mulish",sans-serif}
.header-band{position:absolute;left:0;top:0;width:1200px;height:304px;background:linear-gradient(var(--teal-top),var(--teal-bottom))}
.brand{position:absolute;left:172px;top:30px;display:flex;align-items:center;gap:10px;color:var(--white);font-size:35px;font-weight:400;letter-spacing:0.5px}
.brand-mark{width:30px;height:30px;border-radius:50%;background:var(--white)}
.main-nav{position:absolute;right:184px;top:43px;display:flex;gap:28px}
.main-nav a{color:var(--white);text-decoration:none;font-size:16px;font-weight:400}
.hero{position:absolute;left:174px;top:95px;width:852px;height:419px;background:linear-gradient(120deg,#3a3548 0%,#6a5a48 35%,#2c5fa0 62%,#8a6a40 100%);border:1px solid #3355aa}
.hero-caption{position:absolute;left:161px;top:160px;width:529px;height:94px;background:var(--caption-bg);color:var(--white);font-size:37px;font-weight:400;display:flex;align-items:center;justify-content:center}
.hero-dots{position:absolute;left:385px;top:397px;display:flex;gap:4px}
.hero-dots span{width:11px;height:11px;border-radius:50%;background:var(--white)}
.card{position:absolute;top:540px;width:275px;height:188px}
.card-photo{position:absolute;inset:0}
.card-band{position:absolute;left:0;bottom:0;width:100%;height:44px;background:var(--card-band);color:var(--white);font-size:18px;font-weight:500;padding-left:20px;display:flex;align-items:center}
.card-band svg{position:absolute;right:12px;top:11px}
.card-1{left:174px}.card-1 .card-photo{background:linear-gradient(135deg,#3a3a3a,#6a5040 60%,#8a3a30)}
.card-2{left:463px}.card-2 .card-photo{background:linear-gradient(135deg,#4a4a80,#2a5fb0 55%,#7a7a88)}
.card-3{left:751px}.card-3 .card-photo{background:linear-gradient(135deg,#6a6a5a,#2a50b0 55%,#7a6a60)}
.divider{position:absolute;left:174px;top:740px;width:852px;height:27px;background:linear-gradient(transparent,#f3f3f3);border-bottom:1px solid #e6e6e6}
.intro{position:absolute;left:175px;top:810px;width:470px}
.intro h1{font-size:28px;font-weight:400;color:var(--heading);white-space:nowrap}
.intro h2{font-size:20px;font-weight:300;color:var(--sub);margin-top:4px}
.intro p{font-size:12px;font-weight:300;color:var(--body);line-height:19px;margin-top:10px;width:452px}
.btn-more{position:absolute;left:175px;top:971px;width:100px;height:29px;border-radius:3px;background:linear-gradient(var(--orange-top),var(--orange-bottom));color:var(--white);font-size:12px;font-weight:500;display:flex;align-items:center;justify-content:center}
.video-frame{position:absolute;left:699px;top:804px;width:329px;height:213px;background:var(--white);border:1px solid #e2e2e2;box-shadow:0 1px 3px rgba(0,0,0,0.12)}
.video-still{position:absolute;left:7px;top:7px;width:315px;height:199px;background:linear-gradient(135deg,#d8eef8,#7ab8d8 50%,#1e7fa8)}
.play{position:absolute;left:140px;top:81px}
.site-footer{position:absolute;left:0;top:1066px;width:1200px;height:100px;background:var(--footer-bg);border-top:1px solid var(--footer-line)}
.footer-nav{position:absolute;left:175px;top:27px;font-size:12.5px;color:var(--footer-text);display:flex;gap:6px}
.footer-nav .sep{color:var(--footer-text)}
.copyright{position:absolute;left:175px;top:52px;font-size:11px;color:var(--footer-muted);font-weight:300}
.social{position:absolute;left:940px;top:27px;display:flex;gap:8px}
.social span{width:21px;height:21px;border-radius:2px;background:var(--social)}
</style>
</head>
<body>
<header class="header-band">
  <div class="brand"><span class="brand-mark"></span>Corvella</div>
  <nav class="main-nav">
    <a href="#">About Us</a><a href="#">Services</a><a href="#">Products</a><a href="#">Video</a><a href="#">Support</a><a href="#">Contact</a>
  </nav>
</header>

<section class="hero" role="img" aria-label="Welder in protective mask working with sparks in a workshop">
  <div class="hero-caption">Innovative. Reliable. Flexible</div>
  <div class="hero-dots"><span></span><span></span><span></span><span></span></div>
</section>

<a class="card card-1"><div class="card-photo" role="img" aria-label="Welder in mask working at a bench"></div>
  <div class="card-band">WHAT WE DO<svg width="14" height="24" viewBox="0 0 14 24"><path d="M2 1l10 11L2 23" stroke="#fff" stroke-width="1.6" fill="none"/></svg></div></a>
<a class="card card-2"><div class="card-photo" role="img" aria-label="Automated welding torch on metal"></div>
  <div class="card-band">SERVICES PROVIDE<svg width="14" height="24" viewBox="0 0 14 24"><path d="M2 1l10 11L2 23" stroke="#fff" stroke-width="1.6" fill="none"/></svg></div></a>
<a class="card card-3"><div class="card-photo" role="img" aria-label="Smiling worker in blue overalls"></div>
  <div class="card-band">CASE STUDIES<svg width="14" height="24" viewBox="0 0 14 24"><path d="M2 1l10 11L2 23" stroke="#fff" stroke-width="1.6" fill="none"/></svg></div></a>

<div class="divider"></div>

<section class="intro">
  <h1>Phasellus felis dolor scelerisque tempus</h1>
  <h2>Etiam nulla massa pharetra facilisis volutpat</h2>
  <p>Etiam est nunc venenatis in tristique eu imperdiet ac nisl Cum sociis natoque penatibus et magnis dis parturient montes nascetur ridiculus mus In iaculis facilisis massa Etiam eu urna Sed porta Suspendisse quam leo molestie sed luctus quis feugiat in pede Fusce tellus Sed metus augue convallis</p>
</section>
<a class="btn-more">READ MORE</a>

<figure class="video-frame">
  <div class="video-still" role="img" aria-label="Automated welding cell in a bright factory hall">
    <svg class="play" width="36" height="36" viewBox="0 0 36 36"><circle cx="18" cy="18" r="17" fill="#111" stroke="#fff" stroke-width="1.5"/><path d="M14 11l11 7-11 7z" fill="#fff"/></svg>
  </div>
</figure>

<footer class="site-footer">
  <nav class="footer-nav">
    <span>HOME</span><span class="sep">|</span><span>ABOUT US</span><span class="sep">|</span><span>SERVICES</span><span class="sep">|</span><span>SUPPORT</span><span class="sep">|</span><span>VIDEO</span><span class="sep">|</span><span>TESTIMONIALS</span><span class="sep">|</span><span>CONTACT</span>
  </nav>
  <div class="copyright">© 2014 Company Name &nbsp;All right reserved &nbsp;Term of Use</div>
  <div class="social"><span></span><span></span><span></span></div>
</footer>
</body>
</html>
```